Webdesign for Dutch IT consultancy company

Make a Wordpress webdesign for a Dutch consultancy company

Briefing Brivola IT

Website for finding and connecting IT-professionals. Corebusiness is to find IT-professionals and to help them to follow their ambitions. We offer training, personal coaching and education trajects.

U can take www.Tavemko.nl as an example for the website.

Home page

U can take www.Tavemko.nl as an example.

There should be jobs on the home page. A block for short info about us and about what whe do and a trigger to contact us quickly.

Jobs Page

On this page should be the jobs that we offer for the professionals. There should be a search function on this page so u can easily find the job that you are looking for.

A call to action can be on this page too.

Also a little block with text for some information.

For professionals page

Block with information on top. Call to action. info about who we work for/with.

For Clients

Info about three different solutions

- Sourcing solutions
- Consultancy solutions
- Custom based traineeships

Request a qoute option

Traineeships page

Info about two different traineeships

- Linux traineeships
- Microsoft traineeships

Call to action/ subscribe for traineeships

About us page

We are BrivolaT IT

Our mission: Creating cooperations between young professionals and businesses who wanna work on a great future.

Our core values

Last news

Target Market(s)

Young professionals and businesses who need IT services

Industry/Entity Type

It Company

Coding

Coded - Design and coding required

Number of Pages Required

5+ page

Font styles to use
Other font styles liked:
• Calibri

Colors
ffffff
add136
6b449b

Requirements
Must have
• Home page, Jobs Page, Professionals page, Clients page, Traineeships page, About us Page
• Green and/or Purple layout. Job search option, subscribe option
Nice to have
• modern design

```html
<!DOCTYPE html>
<html lang="en">
<head>
<meta charset="utf-8">
<title>JavaScript Developer Required – Brivola IT</title>
<link rel="stylesheet" href="https://fonts.googleapis.com/css2?family=Raleway:wght@400;500;600;700&display=swap">
<style>
:root{
  --ink:#333333;
  --text:#555555;
  --muted:#8a8a8a;
  --line:#e6e6e6;
  --field:#d9d9d9;
  --accent:#f26522;
  --link:#3f86d6;
  --teal:#2aa6b8;
  --purple:#6b449b;
  --header:#232325;
  --footer:#535353;
  --footer-text:#d6d6d6;
  --white:#ffffff;
}
*{box-sizing:border-box;margin:0;padding:0}
html,body{width:876px;height:1200px;overflow:hidden}
body{position:relative;background:var(--white);font-family:"Raleway",sans-serif;color:var(--text)}
.abs{position:absolute}

/* header */
.site-header{position:absolute;left:0;top:0;width:876px;height:176px;overflow:hidden}
.hero-photo{position:absolute;inset:0;background:linear-gradient(100deg,#1b1b1d 0%,#34353a 35%,#202123 60%,#3a3b40 85%,#1c1c1e 100%)}
.brand{position:absolute;left:127px;top:5px;font-weight:700;font-size:15px;letter-spacing:1px;color:var(--purple);display:flex;align-items:center;gap:5px}
.brand-mark{width:9px;height:9px;background:var(--purple)}
.main-nav{position:absolute;top:8px;left:362px;display:flex;gap:24px;font-size:7.4px;font-weight:500;color:var(--white);text-transform:uppercase}
.btn-signin{position:absolute;left:689px;top:6px;width:56px;height:20px;background:var(--accent);color:var(--white);font-size:8px;font-weight:600;display:flex;align-items:center;justify-content:center;text-transform:uppercase;letter-spacing:.4px}
.page-title{position:absolute;left:126px;top:73px;font-size:27px;font-weight:600;color:var(--white)}

/* company */
.company-logo{position:absolute;left:126px;top:204px;width:77px;height:58px;border:1px solid var(--line);display:flex;align-items:center;justify-content:center;font-weight:700;font-size:14px;color:#2b4a8b}
.company-name{position:absolute;left:216px;top:202px;font-size:8.5px;color:var(--link)}
.meta{position:absolute;left:216px;font-size:7px;color:var(--text);display:flex;align-items:center;gap:5px}
.meta .dot{width:7px;height:7px;border-radius:50%;background:#d3d3d3;display:inline-block}
.share{position:absolute;left:643px;top:218px;display:flex;align-items:center;gap:3px;font-size:8px;color:var(--muted)}
.share span.lbl{margin-right:6px}
.share i{width:12px;height:12px;border-radius:50%;display:inline-block}
.divider{position:absolute;left:126px;width:624px;height:1px;background:var(--line)}

/* overview */
.col-title{position:absolute;font-size:8.4px;color:var(--ink);letter-spacing:.3px}
.overview{position:absolute;left:126px;top:311px;width:270px;font-size:8.3px;line-height:12.6px;color:var(--text)}
.overview p{margin-bottom:5px}
.overview h4{font-size:8.4px;font-weight:600;color:var(--ink);margin-top:-4px;margin-bottom:5px}
.skills{list-style:none;margin-top:7px;font-size:7px;line-height:12.6px}
.skills li{padding-left:7px;position:relative}
.skills li::before{content:"";position:absolute;left:0;top:6px;width:2px;height:2px;background:var(--muted)}

/* job detail */
.detail-list{position:absolute;left:410px;top:318px;width:127px;list-style:none}
.detail-list li{height:33px;border-bottom:1px solid var(--line);display:flex;align-items:center;gap:9px;font-size:7px;line-height:10.5px}
.detail-list svg{width:11px;height:11px;flex:none}
.detail-list .k{color:var(--text)}
.detail-list .v{color:var(--ink);font-weight:500}
.action{position:absolute;left:410px;width:104px;height:20px;border:1px solid var(--link);color:var(--link);font-size:7.3px;display:flex;align-items:center;gap:4px;padding-left:7px}
.action svg{width:8px;height:8px}
.note{position:absolute;left:410px;top:617px;width:130px;font-size:5.8px;line-height:9.6px;color:var(--muted)}

/* contact */
.contact-box{position:absolute;left:553px;top:315px;width:197px;height:276px;border:1px solid #f0f0f0}
.field{position:absolute;left:9px;width:179px;height:23px;border:1px solid var(--field);font-size:6.2px;color:#b5b5b5;padding:7px 7px;display:flex;justify-content:space-between}
.field i{width:6px;height:6px;background:#c8c8c8;display:inline-block}
.field.msg{height:69px}
.captcha{position:absolute;left:9px;top:168px;width:174px;height:44px;border:1px solid var(--field);background:#fafafa;font-size:7px;color:var(--ink)}
.captcha .box{position:absolute;left:8px;top:13px;width:15px;height:15px;border:2px solid #c1c1c1;background:var(--white)}
.captcha .robot{position:absolute;left:30px;top:18px}
.captcha .reload{position:absolute;left:95px;top:16px;font-size:6.5px}
.captcha .seal{position:absolute;left:140px;top:6px;width:16px;height:16px;background:#a7b8d9}
.captcha .seal-t{position:absolute;left:134px;top:27px;font-size:4.5px;color:var(--muted);text-align:center;width:30px;line-height:7px}
.btn-send{position:absolute;left:9px;top:219px;width:179px;height:30px;background:var(--accent);color:var(--white);font-size:7.8px;display:flex;align-items:center;justify-content:center}
.terms{position:absolute;left:0;top:256px;width:197px;text-align:center;font-size:6.3px;color:var(--muted)}
.terms b{font-weight:500;color:var(--ink)}

.safety{position:absolute;left:553px;top:603px;width:197px;height:128px;background:#fbfbfb;overflow:hidden}
.safety h5{position:absolute;left:13px;top:12px;font-size:9.4px;font-weight:500;color:var(--accent);letter-spacing:.4px;display:flex;align-items:center;gap:3px}
.safety .colA,.safety .colB{position:absolute;top:33px;font-size:7.3px;line-height:12.6px;color:var(--ink);white-space:nowrap;overflow:hidden}
.safety .colA{left:13px;width:110px;direction:rtl;text-align:left}
.safety .colA span{direction:ltr;unicode-bidi:embed;display:block}
.safety .colB{left:123px;width:62px}
.safety .bg-tri{position:absolute;left:155px;top:95px}

/* related */
.related-title{position:absolute;left:126px;top:863px;font-size:10px;color:var(--ink);letter-spacing:.4px}
.related-row{position:absolute;left:126px;width:413px;height:30px;display:flex;align-items:center;font-size:8.4px;color:var(--ink)}
.related-row .on{color:#c0c0c0;font-size:7px;margin:0 6px 0 4px}
.related-row .date{color:var(--muted);font-size:7px}
.related-row .tag{margin-left:auto;font-size:6px;text-decoration:underline;text-transform:uppercase}

/* footer */
.site-footer{position:absolute;left:0;top:964px;width:876px;height:236px;background:var(--footer);color:var(--footer-text)}
.f-col{position:absolute;top:34px}
.f-col h3{font-size:12.5px;font-weight:500;color:var(--white);margin-bottom:9px}
.f-col ul{list-style:none;font-size:8px;line-height:15.3px}
.f-about p{font-size:7.8px;line-height:12px;width:130px}
.signature{width:50px;height:20px;margin:8px 0 6px;background:linear-gradient(90deg,rgba(255,255,255,.35),rgba(255,255,255,.12))}
.f-about .name{font-size:8px;color:var(--white);text-transform:uppercase}
.f-about .role{font-size:6.5px;margin-top:3px}
.connect-row{display:flex;align-items:flex-start;gap:10px;font-size:7.8px;line-height:13px;margin-bottom:8px}
.connect-row .ico{width:19px;height:19px;background:#474747;flex:none;display:flex;align-items:center;justify-content:center}
.connect-row .ico.tall{height:46px}
.hours{font-size:8px;color:var(--white);margin-top:8px}
.hours small{display:block;font-size:6.7px;margin-top:3px;color:var(--white)}
</style>
</head>
<body>

<header class="site-header">
  <div class="hero-photo" role="img" aria-label="Dark blurred photo of people in an office meeting"></div>
  <div class="brand"><span class="brand-mark"></span>BRIVOLA IT</div>
  <nav class="main-nav"><span>About us</span><span>Job List</span><span>Solutions</span><span>Traineeships</span><span>Contact us</span></nav>
  <div class="btn-signin">Sign in</div>
  <h1 class="page-title">JavaScript Developer Required</h1>
</header>

<div class="company-logo">NORVEX</div>
<div class="company-name">Kelmor</div>
<div class="meta" style="top:218px"><span class="dot"></span>18 Harlow Crescent, London, NW4 2TP</div>
<div class="meta" style="top:233px"><span class="dot"></span>Post Date: May 29, 2015 <span class="dot" style="margin-left:6px"></span>Applications 1 <span class="dot" style="margin-left:6px"></span>Views 402</div>
<div class="share"><span class="lbl">Share</span><i style="background:#3b5998"></i><i style="background:#1da1f2"></i><i style="background:#ea4c89"></i><i style="background:#b07a55"></i></div>
<div class="divider" style="top:278px"></div>

<div class="col-title" style="left:126px;top:295px">Job Overview</div>
<div class="col-title" style="left:410px;top:295px">Job Detail</div>
<div class="col-title" style="left:553px;top:295px">Contact</div>

<section class="overview">
  <p>Far much that one rank beheld bluebird after outside ignobly allegedly more when oh arrogantly vehement irresistibly fussy penguin insect additionally wow absolutely crud meretriciously hastily dalmatian a glowered inset one echidna cassowary some parrot and much as goodness some froze the sullen much connected bat wonderfully on instantaneously eel valiantly petted this along across highhandedly much dog out the much alas evasively neutral lazy reset.</p>
  <p>Repeatedly dreamed alas opossum but dramatically despite expeditiously that jeepers loosely yikes that as or eel underneath kept and slept compactly far purred sure abidingly up above fitting to strident wiped set waywardly far the and pangolin horse approving paid chuckled cassowary oh above a much opposite far much hypnotically more therefore wasp less that hey apart well like while superbly orca and far hence one.Far much that one rank beheld bluebird after outside ignobly allegedly more when oh arrogantly vehement irresistibly fussy penguin insect additionally wow absolutely crud meretriciously hastily dalmatian a glowered inset one echidna cassowary some parrot and much as goodness some froze the sullen much connected bat wonderfully on instantaneously eel valiantly petted this along across highhandedly much dog out the much alas evasively neutral lazy reset.</p>
  <p>Repeatedly dreamed alas opossum but dramatically despite expeditiously that jeepers loosely yikes that as or eel underneath kept and slept compactly far purred sure abidingly up above fitting to strident wiped set waywardly far the and.</p>
  <h4>Skills Required</h4>
  <p>Far much that one rank beheld bluebird after outside ignobly allegedly more when oh arrogantly vehement irresistibly fussy penguin insect additionally wow absolutely crud meretriciously hastily dalmatian a glowered inset one echidna cassowary some parrot and much as goodness some froze the sullen much connected bat wonderfully on instantaneously. Far much that one rank beheld bluebird after outside ignobly allegedly more when oh arrogantly vehement irresistibly fussy penguin insect additionally.</p>
  <ul class="skills">
    <li>Strong Market connections for business development of the bank.</li>
    <li>Strong knowledge of Corporate products and regulatory requirements.</li>
    <li>Proficiency in spoken and written English.</li>
    <li>Analytical skills</li>
    <li>Knowledge of Corporate Banking, Risk Management, Compliance and Central Bank regulations.</li>
  </ul>
</section>

<ul class="detail-list">
  <li><svg viewBox="0 0 12 12"><path d="M2 6l4-4h4v4l-4 4z" fill="none" stroke="#444" stroke-width="1"/></svg><div><div class="k">Offerd Salary</div><div class="v">£15,000 - £20,000</div></div></li>
  <li><svg viewBox="0 0 12 12"><path d="M1 6l10-5-4 10-1-4z" fill="none" stroke="#444"/></svg><div><div class="k">Career Level</div><div class="v">Student</div></div></li>
  <li><svg viewBox="0 0 12 12"><path d="M1 4l5-2 5 2-5 2zM3 5v3l3 1 3-1V5" fill="none" stroke="#444"/></svg><div><div class="k">Experience</div><div class="v">3 Years</div></div></li>
  <li><svg viewBox="0 0 12 12"><circle cx="6" cy="4" r="2.5" fill="none" stroke="#444"/><path d="M1 11c1-3 9-3 10 0" fill="none" stroke="#444"/></svg><div><div class="k">Gender</div><div class="v">Female</div></div></li>
  <li><svg viewBox="0 0 12 12"><path d="M1 10l3-4 3 2 4-5" fill="none" stroke="#444"/></svg><div><div class="k">INDUSTRY</div><div class="v">Html Department</div></div></li>
  <li><svg viewBox="0 0 12 12"><path d="M0 5l6-3 6 3-6 3z" fill="#444"/><path d="M3 6.5v2.5l3 1.5 3-1.5V6.5" fill="#444"/></svg><div><div class="k">Qualification</div><div class="v">Master's Degree</div></div></li>
</ul>

<div class="action" style="top:536px"><svg viewBox="0 0 10 10"><path d="M5 9L1 5a2 2 0 014-3 2 2 0 014 3z" fill="none" stroke="currentColor"/></svg>Shortlist</div>
<div class="action" style="top:562px"><svg viewBox="0 0 10 10"><rect x="0.5" y="3" width="9" height="6" fill="currentColor"/><rect x="3" y="1" width="4" height="2.5" fill="none" stroke="currentColor"/></svg>Apply Now</div>
<div class="action" style="top:589px"><svg viewBox="0 0 10 10"><rect width="10" height="10" fill="currentColor"/></svg>Apply with Netprofile</div>
<div class="note">Never pay anyone for job application test or interview.</div>

<aside class="contact-box">
  <div class="field" style="top:8px">Enter your Name*<i></i></div>
  <div class="field" style="top:36px">Email Address*<i></i></div>
  <div class="field" style="top:64px">Phone Number<i></i></div>
  <div class="field msg" style="top:93px">Message should have more than 50 characters</div>
  <div class="captcha">
    <span class="box"></span><span class="robot">I'm not a robot</span>
    <span class="reload">&#8635; Reload</span>
    <span class="seal"></span><span class="seal-t">Verify<br>Privacy - Terms</span>
  </div>
  <div class="btn-send">Send Email</div>
  <div class="terms">You accepts our <b>Terms and Conditions</b></div>
</aside>

<aside class="safety">
  <h5><svg width="9" height="8" viewBox="0 0 9 8"><path d="M4.5 0L9 8H0z" fill="var(--accent)"/><rect x="4" y="2.5" width="1" height="3" fill="#fff"/><rect x="4" y="6" width="1" height="1" fill="#fff"/></svg>Safety Information</h5>
  <div class="colA"><span>Dear Candidate</span><span>Important details should not be</span><span>given when applying for a job.</span><span>We are not responsible for any</span><span>external content. All applications</span><span>should go via the 'Apply now' button.</span></div>
  <div class="colB">Safety Tips For<br>Far much that one<br>after outside ignobly<br>oh arrogantly vehement<br>penguin insect<br>crud meretriciously</div>
  <svg class="bg-tri" width="44" height="40" viewBox="0 0 44 40"><path d="M22 0L44 40H0z" fill="#f26522" opacity=".12"/></svg>
</aside>

<div class="related-title">Related Jobs (2)</div>
<div class="divider" style="top:886px;width:413px"></div>
<div class="related-row" style="top:887px">Operational Manager Part Time<span class="on">on</span><span class="date">May 29, 2015</span><span class="tag" style="color:var(--link)">Temporary</span></div>
<div class="divider" style="top:917px;width:413px"></div>
<div class="related-row" style="top:917px">Application Developer For Android<span class="on">on</span><span class="date">July 29, 2015</span><span class="tag" style="color:var(--teal)">Part time</span></div>

<footer class="site-footer">
  <div class="f-col f-about" style="left:126px">
    <h3>About Us</h3>
    <p>Lorem ipsum dolor sit amet, consectetuer adipiscing elit. Donec odio. Quisque volutpat mattis eros. Nullam malesuada erat ut turpis.</p>
    <div class="signature" role="img" aria-label="Handwritten signature"></div>
    <div class="name">Marten Holde</div>
    <div class="role">CEO</div>
  </div>
  <div class="f-col" style="left:286px">
    <h3>Job Seekers</h3>
    <ul><li>Local Jobbs</li><li>Company Directory</li><li>Browse Jobs</li><li>Salary Estimator</li><li>Resume Designer</li><li>Consultancy</li><li>Help</li></ul>
  </div>
  <div class="f-col" style="left:393px">
    <h3>Employers</h3>
    <ul><li>Top Talent</li><li>Groups</li><li>Employee managemnt</li><li>Human Resource</li><li>Hiring Agents</li><li>Discussion Forums</li><li>Suggestions</li></ul>
  </div>
  <div class="f-col" style="left:499px">
    <h3>Site Map</h3>
    <ul><li>Product</li><li>Terms &amp; Policies</li><li>FAQ's</li><li>Jobs Packages</li><li>CV Packages</li></ul>
  </div>
  <div class="f-col" style="left:606px">
    <h3>Connect</h3>
    <div class="connect-row"><span class="ico"><svg width="9" height="9" viewBox="0 0 10 10"><path d="M2 0l2 2-1 1.5 3.5 3.5L8 6l2 2-2 2C4 10 0 6 0 2z" fill="#fff"/></svg></span><span style="padding-top:3px">+1 555 204 7731</span></div>
    <div class="connect-row"><span class="ico"><svg width="10" height="8" viewBox="0 0 10 8"><rect width="10" height="8" fill="#fff"/><path d="M0 0l5 4 5-4" fill="none" stroke="#474747"/></svg></span><span style="padding-top:3px">hello@lumenforge.com</span></div>
    <div class="connect-row"><span class="ico tall"><svg width="8" height="11" viewBox="0 0 8 11"><path d="M4 11L1 6a3.5 3.5 0 116 0z" fill="#fff"/><circle cx="4" cy="4" r="1.3" fill="#474747"/></svg></span><span>12 – C, 3rd Floor, Alder Court Residences, Kent, UK. 41BK902D.</span></div>
    <div class="hours">OFFICE HOURS<small>9:00 AM - 6:00 PM MON - FRI</small></div>
  </div>
</footer>

</body>
</html>
```